Moder Business Card Design for Renewables Business

Need a business card design for my business. We collect & repurpose spent coffee ground from cafes. The cards will be made from recycled paper. Needs to fit our corporate colour scheme of white, green & brown (see logo for colour codes). Eco friendly, modern, intresting & eye catching.
This card needs to convey the message of the business and fit into its mantra of eco-friendly, sustainable etc.

Target Market(s)

Cafe Owners, Coffee Drinkers, Recycling Companies, Farmers

Industry/Entity Type

Recycling

Contact Information for Business Card

Name; Peter Halloran
Phone; 0412 386 527
e-mail; info@lumatrove.com.au
website; www.lumatrove.com.au

Font styles to use
Sans Serif
Script

Colors

Designer to choose colors to be used in the design.

Requirements
Must have
• FRONT;
• Logo, Name (Peter Halloran), phone number, e-mail address, website
• BACK;
• On the back in cursive text; 'GIVING EVERY CUP A SECOND LIFE'
• Small facebook & Instagram logos with text 'Lumatrove'
Should not have
• messy design

```html
<!DOCTYPE html>
<html lang="en">
<head>
<meta charset="utf-8">
<title>Lumatrove Business Card</title>
<link href="https://fonts.googleapis.com/css2?family=Montserrat:wght@400;500;600;800&family=Roboto+Condensed:wght@700&display=swap" rel="stylesheet">
<style>
  :root {
    --backdrop: #2b2b2c;
    --kraft: #d9ccb1;
    --kraft-deep: #c9ba9b;
    --coffee: #5a3522;
    --coffee-dark: #4a2b1b;
    --leaf: #6a9a4a;
    --leaf-soft: #7daa5a;
    --ink: #2e1f17;
    --paper-white: #f4efe6;
  }
  * { margin: 0; padding: 0; box-sizing: border-box; }
  html, body {
    width: 1200px; height: 900px; overflow: hidden;
    background: var(--backdrop);
    font-family: "Montserrat", Arial, sans-serif;
  }
  .stage {
    position: relative; width: 1200px; height: 900px;
    display: flex; justify-content: center; align-items: center; gap: 60px;
  }
  .card {
    position: relative; width: 360px; height: 630px; overflow: hidden;
    background: radial-gradient(circle at 40% 30%, #ded2b8 0%, var(--kraft) 55%, var(--kraft-deep) 100%);
    box-shadow: 0 18px 40px rgba(0,0,0,.45);
  }
  .wordmark {
    position: absolute; left: 0; right: 0; text-align: center;
    font-family: "Montserrat", Arial, sans-serif; font-weight: 800;
    color: var(--leaf); letter-spacing: 1px; text-transform: uppercase;
    white-space: nowrap;
  }
  .wordmark-dot {
    display: inline-block; width: 14px; height: 14px; border-radius: 50%;
    background: var(--coffee); margin-right: 10px; vertical-align: middle;
    position: relative; top: -3px;
  }
  .band-line {
    position: absolute; left: 0; right: 0; height: 6px; background: var(--leaf);
  }
  .band {
    position: absolute; left: 0; right: 0; bottom: 0; background: var(--coffee);
  }

  /* back card */
  .card-back .wordmark { top: 330px; font-size: 36px; }
  .tagline {
    position: absolute; left: 0; right: 0; top: 478px; text-align: center;
    font-family: "Roboto Condensed", Arial, sans-serif; font-weight: 700;
    font-size: 19px; color: var(--ink); letter-spacing: .3px;
    white-space: nowrap;
  }
  .card-back .band-line { top: 508px; }
  .card-back .band { top: 518px; }
  .social-list {
    list-style: none; position: absolute; left: 40px; top: 540px;
    color: var(--paper-white); font-size: 16px;
  }
  .social-list li { display: flex; align-items: center; gap: 12px; margin-bottom: 12px; }
  .social-marker {
    width: 16px; height: 16px; border: 2px solid var(--paper-white); border-radius: 50%;
  }

  /* front card */
  .card-front .wordmark { top: 170px; font-size: 34px; }
  .card-front .band-line { top: 268px; }
  .card-front .band { top: 278px; }
  .divider {
    position: absolute; left: 0; right: 0; top: 300px; height: 2px;
    background: var(--coffee-dark); box-shadow: 0 1px 0 rgba(255,255,255,.08);
  }
  .person-name {
    position: absolute; left: 0; right: 0; top: 336px; text-align: center;
    font-size: 24px; font-weight: 500; letter-spacing: 3px; text-transform: uppercase;
    color: var(--paper-white);
  }
  .person-name .first { color: var(--leaf-soft); }
  .contact-list {
    list-style: none; position: absolute; left: 62px; top: 410px;
    color: var(--paper-white); font-size: 16px;
  }
  .contact-list li { display: flex; align-items: center; gap: 14px; margin-bottom: 14px; }
  .contact-icon {
    width: 24px; height: 24px; border-radius: 5px; background: var(--leaf);
    display: flex; align-items: center; justify-content: center;
  }
  .contact-icon svg { width: 15px; height: 15px; }
</style>
</head>
<body>
<main class="stage">

  <section class="card card-back" aria-label="Card back">
    <div class="wordmark"><span class="wordmark-dot"></span>Lumatrove</div>
    <p class="tagline">GIVING EVERY CUP A SECOND LIFE</p>
    <div class="band-line"></div>
    <div class="band"></div>
    <ul class="social-list">
      <li><span class="social-marker"></span>lumatrove.social/news</li>
      <li><span class="social-marker"></span>lumatrove.social/photos</li>
    </ul>
  </section>

  <section class="card card-front" aria-label="Card front">
    <div class="wordmark"><span class="wordmark-dot"></span>Lumatrove</div>
    <div class="band-line"></div>
    <div class="band"></div>
    <div class="divider"></div>
    <h1 class="person-name"><span class="first">Peter</span> Halloran</h1>
    <ul class="contact-list">
      <li>
        <span class="contact-icon">
          <svg viewBox="0 0 24 24"><path fill="#f4efe6" d="M6.6 10.8a15.1 15.1 0 0 0 6.6 6.6l2.2-2.2a1 1 0 0 1 1-.25 11.4 11.4 0 0 0 3.6.57 1 1 0 0 1 1 1V20a1 1 0 0 1-1 1A17 17 0 0 1 3 4a1 1 0 0 1 1-1h3.5a1 1 0 0 1 1 1c0 1.25.2 2.45.57 3.57a1 1 0 0 1-.25 1z"/></svg>
        </span>0412 386 527
      </li>
      <li>
        <span class="contact-icon">
          <svg viewBox="0 0 24 24"><rect x="3" y="6" width="18" height="12" rx="1.5" fill="#f4efe6"/><path d="M3.5 6.8 12 13l8.5-6.2" fill="none" stroke="#6a9a4a" stroke-width="1.8"/></svg>
        </span>info@lumatrove.com.au
      </li>
      <li>
        <span class="contact-icon">
          <svg viewBox="0 0 24 24" fill="none" stroke="#f4efe6" stroke-width="2"><circle cx="12" cy="12" r="8.5"/><ellipse cx="12" cy="12" rx="3.8" ry="8.5"/><path d="M3.5 12h17"/></svg>
        </span>www.lumatrove.com.au
      </li>
    </ul>
  </section>

</main>
</body>
</html>
```